πΈ Full Website Redesign on Wix β The Quillmere Nook (Feminine, Sophisticated, Nature-Inspired)
Business Name: The Quillmere Nook
Current Site: https://lnkhop.to/QzrTwpa (for structure reference only)
Platform: Wix
Business Type: Women-led Canadian online retail business
Location: Canada
π About The Quillmere Nook
The Quillmere Nook is a boutique e-commerce store specializing in roses and blooming plants, created for modern plant lovers who appreciate beauty, quality, and storytelling.
We are a small, women-led business in Ontario, Canada, and our audience is primarily women who are drawn to floral aesthetics, a calming user experience, and elevated design.
Our name β The Quillmere Nook β represents both a curated collection of blooms and a love of thoughtful, meaningful beauty.
π» Project Overview
We are looking for a full website redesign from scratch (built on Wix) that reflects our brand identity: feminine, sophisticated, romantic, and grounded in nature.
The current version of the site was just a test layout β we now want a fresh, cohesive design vision that speaks directly to our female Canadian customer base with a clean, modern, and elegant interface.
This project is not just about functionality β itβs about crafting an experience that feels like a digital floral sanctuary.
π― What We Need
Full website design and development in Wix (you can start fresh)
Custom homepage design with storytelling and a welcoming brand vibe
Pages to include (subject to refinement):
Home
Shop (products will be added by us later)
About
Contact
FAQ / Info
Blog or Guides (optional placeholder)
Sophisticated visual branding:
Muted rose, blush, and earthy tones
Clean, modern layout with elegant typography
Feminine, natural, soft design elements (think floral details, soft lines, minimalism with warmth)
Optimized for both desktop and mobile
Set up global styles (font, color palette, button styles, etc.)
Guidance or setup for product sections using Wixβs eCommerce system
Create beautiful reusable sections (for us to duplicate later as needed)
π· Brand Style
We are aiming for a website that feels like:
A curated botanical boutique
Feminine and warm β but not overly girly
Sophisticated and soft, never cluttered
Clean but not sterile
Relaxed elegance with a focus on natural beauty
Color palette:
Muted rose
Warm blush tones
Cream, soft beige, earthy sage
Very subtle contrast β no stark black-and-white
Typography:
Elegant serif or soft sans-serif pairings
Easy to read but with character
π Technical Info
Platform: Wix
No custom coding required (Wix-native tools preferred)
We will handle product uploads
Weβll provide any imagery you request
π¦ Deliverables
Fully designed Wix website (ready to publish)
All pages complete with consistent design and layout
Mobile-responsive layout
Design system set up for future content (colors, typography, etc.)
Optional: Style guide PDF for brand reference (bonus)
π Timeline
Weβd like the website to be completed within 1-2 weeks after project start. Please let us know your availability.
β
To Apply
Please include:
Portfolio (especially if youβve done Wix, floral, feminine, or nature-inspired work)
A short message on how you'd approach this project
Timeline/availability
We're looking for someone who understands how to design for emotion, beauty, and ease β not just functionality. If you love soft colors, delicate details, and creating meaningful digital experiences for women, we'd love to hear from you.
πΈ Letβs build something beautiful together!
Rose enthusiasts

```html
<!DOCTYPE html>
<html lang="en">
<head>
<meta charset="utf-8">
<title>The Quillmere Nook – Home</title>
<link rel="stylesheet" href="https://fonts.googleapis.com/css2?family=Red+Hat+Display:wght@400;500;600;700&family=Inter:wght@400;500;600&display=swap">
<style>
:root{
  --rose:#d8a6b0;
  --blush-bg:#fbf3f3;
  --plum:#5a3a50;
  --ink:#2f2a2c;
  --muted:#4b4548;
  --white:#ffffff;
  --line:#efd9dd;
}
*{box-sizing:border-box;margin:0;padding:0}
html,body{width:1200px;height:3647px;overflow:hidden}
body{position:relative;background:var(--blush-bg);font-family:"Inter",sans-serif;color:var(--ink)}
.abs{position:absolute}
.heading{font-family:"Red Hat Display",sans-serif}

.promo-bar{top:0;left:0;width:1200px;height:43px;background:var(--rose);color:var(--white);
  display:flex;align-items:center;justify-content:center;gap:8px;font-size:15px;font-weight:500}
.site-header{top:43px;left:0;width:1200px;height:85px;background:var(--white)}
.brand{left:112px;top:15px;display:flex;align-items:center;gap:10px;font-family:"Red Hat Display",sans-serif;font-size:19px;color:var(--plum);font-weight:500}
.brand-mark{width:34px;height:54px;border-radius:4px;background:var(--plum)}
.main-nav{top:0;height:85px;left:428px;display:flex;align-items:center;gap:45px;font-size:16px;color:var(--muted)}
.main-nav .active{color:var(--plum);font-weight:600}
.header-actions{right:110px;top:0;height:85px;display:flex;align-items:center;gap:26px;font-size:16px;font-weight:600;color:var(--plum);font-family:"Red Hat Display",sans-serif}

.hero{top:128px;left:0;width:1200px;height:552px;background:linear-gradient(135deg,#6b2a2a 0%,#3f4a2c 45%,#8a3232 70%,#4b3a2a 100%)}
.hero-title{top:147px;left:0;width:1200px;text-align:center;color:var(--white);font-size:64px;font-weight:700;line-height:78px;letter-spacing:-1px}
.hero-sub{top:308px;left:0;width:1200px;text-align:center;color:var(--white);font-size:26px;font-weight:600}
.btn{display:flex;align-items:center;justify-content:center;font-family:"Inter",sans-serif;font-weight:600;font-size:17px}
.btn-light{border:2px solid var(--white);color:var(--white);background:transparent}
.btn-dark{border:2px solid var(--plum);color:var(--plum);background:transparent}
.hero .btn{top:364px;left:523px;width:152px;height:49px;font-size:16px}

.section-title{left:0;width:1200px;text-align:center;color:var(--plum);font-size:43px;font-weight:500}
.intro{top:822px;left:150px;width:900px;text-align:center;font-size:17px;line-height:31px;color:var(--muted)}
.product{top:935px;width:316px}
.product-photo{width:316px;height:375px}
.product-name{margin-top:22px;font-size:17px;font-weight:600;color:var(--ink)}
.product-price{margin-top:8px;font-size:15px;color:var(--muted)}

.story{top:1579px;left:112px;width:976px;height:487px;background:linear-gradient(160deg,#4a4a3a,#2f3a2c 50%,#5a3a3c)}
.story-title{top:92px;left:0;width:976px;text-align:center;color:var(--white);font-size:44px;font-weight:500}
.story-text{top:155px;left:203px;width:570px;text-align:center;color:var(--white);font-size:15px;line-height:29px}
.story .btn{top:330px;left:397px;width:182px;height:59px}

.insta-row{top:2243px;left:112px;display:flex;width:1088px;height:331px;overflow:hidden}
.insta-tile{flex:0 0 330px;height:331px}
.insta-next{top:2389px;left:1130px;width:36px;height:36px;border-radius:50%;background:rgba(255,255,255,.85);display:flex;align-items:center;justify-content:center}

.newsletter{top:2670px;left:112px;width:976px;height:429px;background:linear-gradient(180deg,#2e3e5a 0%,#34465f 45%,#1e2230 80%,#2a2e3a 100%)}
.newsletter-title{top:82px;left:0;width:976px;text-align:center;color:var(--white);font-size:45px;font-weight:500;line-height:52px}
.newsletter-sub{top:202px;left:0;width:976px;text-align:center;color:var(--white);font-size:15px}
.newsletter .btn{top:255px;left:397px;width:182px;height:59px}

.site-footer{top:3204px;left:0;width:1200px;height:443px;background:var(--rose);color:var(--white)}
.footer-brand{top:90px;left:112px;display:flex;align-items:center;gap:16px;font-family:"Red Hat Display",sans-serif;font-size:26px;font-weight:400}
.footer-mark{width:48px;height:78px;border-radius:5px;background:var(--white)}
.footer-col{top:90px}
.footer-col h3{font-family:"Red Hat Display",sans-serif;font-size:21px;font-weight:500;margin-bottom:8px}
.footer-col li{list-style:none;font-size:15px;line-height:29px}
.footer-divider{top:356px;left:112px;width:976px;height:1px;background:rgba(255,255,255,.45)}
.copyright{top:392px;left:0;width:1200px;text-align:center;font-size:15px}
</style>
</head>
<body>

<div class="abs promo-bar">Free shipping on orders over $200
  <svg width="16" height="15" viewBox="0 0 24 22" fill="none" stroke="#fff" stroke-width="2"><path d="M12 20S2 13.5 2 7.5A5 5 0 0 1 12 5a5 5 0 0 1 10 2.5C22 13.5 12 20 12 20z"/></svg>
</div>

<header class="abs site-header">
  <div class="abs brand"><span class="brand-mark"></span>the quillmere nook</div>
  <nav class="abs main-nav">
    <span class="active">Home</span><span>Shop</span><span>About</span><span>Contact</span><span>FAQ</span><span>Blog</span>
  </nav>
  <div class="abs header-actions">
    <svg width="18" height="18" viewBox="0 0 24 24" fill="#5a3a50"><rect x="3" y="9" width="18" height="4"/><rect x="5" y="13" width="14" height="9"/><rect x="11" y="9" width="2" height="13" fill="#fff"/><path d="M12 9C9 3 5 5 7 8zM12 9c3-6 7-4 5-1z"/></svg>
    <span>Log In</span>
  </div>
</header>

<section class="abs hero" role="img" aria-label="Red climbing roses over an old wooden garden gate">
  <h1 class="abs heading hero-title">Potted Beauty, Ready to<br>Root at Home</h1>
  <p class="abs heading hero-sub">the quillmere nook</p>
  <a class="abs btn btn-light">Shop Now</a>
</section>

<h2 class="abs heading section-title" style="top:752px">Explore the Collection</h2>
<p class="abs intro">The Quillmere Nook is a boutique e-commerce store specializing in roses and blooming plants, created for modern plant lovers who appreciate beauty, quality, and storytelling.</p>

<article class="abs product" style="left:102px">
  <div class="product-photo" role="img" aria-label="Pink roses climbing a white picket fence" style="background:linear-gradient(160deg,#6f8a4a,#e58bb5 50%,#f0eef0)"></div>
  <h3 class="product-name">Hollyfield Beauty</h3>
  <p class="product-price">C$31.99</p>
</article>
<article class="abs product" style="left:442px">
  <div class="product-photo" role="img" aria-label="A single yellow rose in bloom" style="background:radial-gradient(circle at 55% 55%,#f5c21a 0%,#e9b020 35%,#a9b6c2 75%,#c9d3da)"></div>
  <h3 class="product-name">Golden Veldt Rose</h3>
  <p class="product-price">C$31.99</p>
</article>
<article class="abs product" style="left:781px">
  <div class="product-photo" role="img" aria-label="Coral orange rose against green foliage" style="background:radial-gradient(circle at 50% 45%,#f27a5e 0%,#ef6f55 35%,#2f6a4e 80%)"></div>
  <h3 class="product-name">Coral Reverie Rose</h3>
  <p class="product-price">C$31.99</p>
</article>

<a class="abs btn btn-dark" style="top:1445px;left:509px;width:182px;height:59px">Shop Now</a>

<section class="abs story" role="img" aria-label="Soft pink garden roses among dark green leaves">
  <h2 class="abs heading story-title">Our Journey from Seed to Blossom</h2>
  <p class="abs story-text">The Quillmere Nook is dedicated to providing a curated collection of roses and blooming plants, carefully selected to bring joy and elegance to your home garden. Our team is committed to sharing our passion for plants and fostering a community of plant enthusiasts. Join us in celebrating the beauty of nature and the art of plant care.</p>
  <a class="abs btn btn-light">Our Mission</a>
</section>

<h2 class="abs heading section-title" style="top:2150px">Join Us on Bloomfeed</h2>
<div class="abs insta-row">
  <div class="insta-tile" role="img" aria-label="Bouquet of red and pink roses" style="background:linear-gradient(150deg,#c0182a,#e77d8f 55%,#2f4a30)"></div>
  <div class="insta-tile" role="img" aria-label="Florist handing a rose bouquet to a customer" style="background:linear-gradient(150deg,#8a5a40,#c4455a 50%,#2f4a3a)"></div>
  <div class="insta-tile" role="img" aria-label="Pink roses in a sunny garden" style="background:linear-gradient(150deg,#d7d7a0,#ea86b8 55%,#7f9a55)"></div>
  <div class="insta-tile" role="img" aria-label="Orange roses among green leaves" style="background:linear-gradient(150deg,#3f5a35,#f0924a 60%)"></div>
</div>
<div class="abs insta-next">
  <svg width="14" height="14" viewBox="0 0 24 24" fill="none" stroke="#333" stroke-width="3"><path d="M9 4l8 8-8 8"/></svg>
</div>

<section class="abs newsletter" role="img" aria-label="City skyline at dusk reflected on the water">
  <h2 class="abs heading newsletter-title">Stay Informed About Plants and More.<br>No Spam, We Promise.</h2>
  <p class="abs newsletter-sub">Subscribe Now and Enjoy 15% Off Your First Purchase</p>
  <a class="abs btn btn-light">Contact Us</a>
</section>

<footer class="abs site-footer">
  <div class="abs footer-brand"><span class="footer-mark"></span>the quillmere nook</div>
  <div class="abs footer-col" style="left:429px">
    <h3>Shop</h3>
    <ul><li>Shop All</li><li>Plants</li><li>Pots</li><li>Sale</li><li>Gift Card</li><li>Subscriptions</li><li>Care</li></ul>
  </div>
  <div class="abs footer-col" style="left:627px">
    <h3>Helpful Links</h3>
    <ul><li>FAQ</li><li>Shipping &amp; Returns</li><li>Terms &amp; Conditions</li><li>Payment Methods</li></ul>
  </div>
  <div class="abs footer-col" style="left:910px">
    <h3>Company</h3>
    <ul><li>Our Story</li><li>Contact Us</li></ul>
  </div>
  <div class="abs footer-divider"></div>
  <p class="abs copyright">Copyrights@2025.The Quillmere Nook.All Rights Reserved</p>
</footer>

</body>
</html>
```